Lunch Feature Menu and business card design

I am in need of a feature lunch menu for our cafe - 1924 Heron Cafe - I would like it to emulate the design of our current menu. I would also like it on an A5 paper size. I have attached a pdf of our current menu for you to see the style that it needs to follow and I have attached our logo as well which will also need to be on the menu. There are 5 feature items that will be going on the menu. The print for these items has been uploaded

Target Market(s)

downtown business crowd during the week and families on the weekend

Industry/Entity Type

Business

Contact Information for Business Card

cafe name : 1924 Heron Cafe
my name : Marina Tolliver
title: General Manager and Partner
email :marina.tolliver@1924heroncafe.example
phone number : 555.214.7391
address : 42 Wexford Lane Sw Calgary Alberta T0X0X0

Requirements
Nice to have
• Our cafe is a historic landmark in the city. It is very rustic - we would like to merge rustic and modern styles together for the menu and business card.

```html
<!DOCTYPE html>
<html lang="en">
<head>
<meta charset="utf-8">
<title>1924 Heron Cafe – Lunch Feature Menu</title>
<link href="https://fonts.googleapis.com/css2?family=Arvo:wght@400;700&family=Open+Sans:ital@1&display=swap" rel="stylesheet">
<style>
  :root {
    --paper: #efe1b6;
    --ink: #231f1c;
    --accent-red: #e0201b;
    --gold: #c9a066;
    --gold-soft: rgba(201, 160, 102, 0.45);
    --band: #231f1c;
    --band-text: #ffffff;
  }
  * { margin: 0; padding: 0; box-sizing: border-box; }
  html, body { width: 846px; height: 1200px; overflow: hidden; background: var(--paper); }
  .menu {
    position: relative;
    width: 846px;
    height: 1200px;
    background: var(--paper);
    color: var(--ink);
    font-family: "Arvo", serif;
    text-align: center;
  }
  .corner-flourish {
    position: absolute;
    width: 190px;
    height: 150px;
    background: radial-gradient(ellipse at var(--pos), var(--gold-soft) 0%, rgba(201,160,102,0.12) 45%, transparent 70%);
  }
  .corner-flourish.top-left { top: 18px; left: 18px; --pos: 20% 20%; }
  .corner-flourish.top-right { top: 18px; right: 18px; --pos: 80% 20%; }
  .corner-flourish.bottom-left { bottom: 18px; left: 18px; --pos: 20% 80%; }
  .corner-flourish.bottom-right { bottom: 18px; right: 18px; --pos: 80% 80%; }
  .side-flourish {
    position: absolute;
    top: 170px;
    width: 100px;
    height: 70px;
    background: radial-gradient(ellipse at center, var(--gold-soft) 0%, transparent 70%);
  }
  .side-flourish.left { left: 230px; }
  .side-flourish.right { right: 230px; }
  .frame-line {
    position: absolute;
    background: var(--gold);
  }
  .frame-line.top { top: 32px; left: 200px; right: 200px; height: 2px; }
  .frame-line.bottom { bottom: 32px; left: 200px; right: 200px; height: 2px; }
  .frame-line.left { left: 32px; top: 190px; bottom: 190px; width: 2px; }
  .frame-line.right { right: 32px; top: 190px; bottom: 190px; width: 2px; }

  .brand {
    position: absolute;
    top: 150px;
    left: 0;
    right: 0;
    font-size: 34px;
    font-weight: 700;
    color: var(--ink);
    letter-spacing: 0.5px;
  }
  .title-band {
    position: absolute;
    top: 290px;
    left: 271px;
    width: 304px;
    height: 46px;
  }
  .title-band svg { position: absolute; inset: 0; }
  .title-band h1 {
    position: relative;
    line-height: 46px;
    font-size: 21px;
    font-weight: 700;
    color: var(--band-text);
  }
  .items {
    position: absolute;
    top: 372px;
    left: 60px;
    right: 60px;
  }
  .item h2 { font-size: 20px; font-weight: 700; line-height: 26px; }
  .item p { font-size: 15px; line-height: 19px; }
  .addon-note { color: var(--accent-red); font-size: 13.5px; font-weight: 700; margin: 9px 0 8px; }
  .addon-list { font-size: 15px; line-height: 20px; word-spacing: 8px; }
  .divider { width: 7px; height: 7px; background: var(--ink); margin: 8px auto 9px; }
  .footer-note {
    position: absolute;
    top: 1155px;
    left: 0;
    right: 0;
    font-family: "Open Sans", sans-serif;
    font-style: italic;
    font-size: 11.5px;
  }
</style>
</head>
<body>
<main class="menu">
  <div class="corner-flourish top-left" role="img" aria-label="Gold scroll ornament in the corner"></div>
  <div class="corner-flourish top-right" role="img" aria-label="Gold scroll ornament in the corner"></div>
  <div class="corner-flourish bottom-left" role="img" aria-label="Gold scroll ornament in the corner"></div>
  <div class="corner-flourish bottom-right" role="img" aria-label="Gold scroll ornament in the corner"></div>
  <div class="side-flourish left" role="img" aria-label="Gold swirl ornament beside the cafe name"></div>
  <div class="side-flourish right" role="img" aria-label="Gold swirl ornament beside the cafe name"></div>
  <div class="frame-line top"></div>
  <div class="frame-line bottom"></div>
  <div class="frame-line left"></div>
  <div class="frame-line right"></div>

  <div class="brand">1924 Heron Cafe</div>

  <div class="title-band">
    <svg width="304" height="46" viewBox="0 0 304 46" aria-hidden="true">
      <polygon points="10,0 294,0 294,8 304,8 304,38 294,38 294,46 10,46 10,38 0,38 0,8 10,8" fill="var(--band)"/>
    </svg>
    <h1>Lunch Feature Menu</h1>
  </div>

  <section class="items">
    <article class="item">
      <h2>This Spuds For You</h2>
      <p>Our home-style hashbrowns topped with our ooey gooey gouda and rich gravy – 9.00</p>
      <p class="addon-note">Add any of the following items for 1.75</p>
      <p class="addon-list">Cheese Onion Ham Bacon Sausage Mushrooms<br>Sprouts Peach Raisin Pineapple Hot Pepper Green Pepper Tomatoes<br>Avocado Spinach Cucumber Feta Cheese Cottage Cheese</p>
    </article>
    <div class="divider"></div>
    <article class="item">
      <h2>Eggstra , Eggstra! Eat All About It!</h2>
      <p>A twist on a classic! Creamy avocado egg salad between 2 slices of whole wheat toast with a<br>dash of Dijon to spice up your life! Served with our 1924 home-style hashbrowns - 13.00</p>
    </article>
    <div class="divider"></div>
    <article class="item">
      <h2>The Steakout</h2>
      <p>An 8 0z Angus rib-eye grilled to your liking served open faced on whole wheat toast and<br>topped with caramelized onions and melted ooey gooey gouda. Served with a side of tangy<br>horseradish spread alongside our 1924 home-style hashbrowns – 19.00</p>
    </article>
    <div class="divider"></div>
    <article class="item">
      <h2>The Kickin’ Chicken</h2>
      <p>Grilled flour tortilla stuffed with chicken, bacon, onions, pineapple and oooey gooey gouda<br>all topped off with a tangy BBQ sauce - the perfect sweet and savory combination! Served<br>with a side of salsa and sour cream – 12.00<br>Include hashbrowns with your quesadilla – 4.00</p>
    </article>
    <div class="divider"></div>
    <article class="item">
      <h2>The Big Cheese</h2>
      <p>Oooey gooey Gouda melted between two slices of whole wheat bread – Have it as is or<br>make it your own! Served with our 1924 home-style hashbrowns – 12.50</p>
      <p class="addon-note">Add any of the following items for 1.75</p>
      <p class="addon-list">Cheese Onion Ham Bacon Sausage Mushrooms<br>Sprouts Peach Raisin Pineapple Hot Pepper Green Pepper<br>Tomatoes Avocado Spinach Cucumber Feta Cheese<br>Cottage Cheese</p>
    </article>
    <div class="divider"></div>
    <article class="item">
      <h2>Baby It's Cold Outside</h2>
      <p>Our delicious, homemade vegetarian Chilli chock-a-block full of hearty veggies and topped<br>with our ooey gooey Gouda. Served with a side of whole wheat toast – 12.00</p>
    </article>
  </section>

  <p class="footer-note">Don't forget to check out our mini museum downstairs!</p>
</main>
</body>
</html>
```